New Business Card Design Project

I need a clean, professional business card. I'd like it to have some color, but not be wild. We do technology consulting and we have clients large and small who trust us with some of their most important data and projects. Simple but not boring should drive all design proposals. Multicolored and two sided, but with a matte finish, I think.
For more on tone, check out our website: http://quorvantis.example

Target Market(s)

Upper management of respected businesses. Tech savvy, but not "hipster".

Industry/Entity Type

Business

Requirements
Must have
• Files need to be provided in .eps and in .pdf in a manner that allows for easy updates.
Must have Name, Title, Phone, Email, Twitter, Website
Nice to have
• Logo/Name shouldn't be too big. One thing I've read several places is that the bigger the logo, the smaller the brand. A good article on dos and don'ts here: http://www.brindlepost.example/2011/02/business-card-experience.html

```html
<!DOCTYPE html>
<html lang="en">
<head>
<meta charset="utf-8">
<title>Quorvantis Business Card</title>
<link rel="stylesheet" href="https://fonts.googleapis.com/css2?family=Dosis:wght@500;600&display=swap">
<style>
  :root {
    --page-bg: #e9e5df;
    --card-bg: #ffffff;
    --teal: #3b92a3;
    --ink-grey: #6e6e6e;
    --name-white: #ffffff;
    --card-shadow: 0 2px 5px rgba(0, 0, 0, 0.22);
  }
  * { margin: 0; padding: 0; box-sizing: border-box; }
  html, body {
    width: 1200px;
    height: 1000px;
    overflow: hidden;
    background: var(--page-bg);
    font-family: "Dosis", "Arial Narrow", sans-serif;
  }
  .card {
    position: absolute;
    top: 348px;
    width: 548px;
    height: 305px;
    background: var(--card-bg);
    box-shadow: var(--card-shadow);
    overflow: hidden;
  }
  .card--front { left: 41px; }
  .card--back { left: 611px; }

  .brand {
    position: absolute;
    left: 0;
    right: 0;
    top: 50%;
    transform: translateY(-50%);
    display: flex;
    align-items: center;
    justify-content: center;
    gap: 12px;
  }
  .brand__square {
    width: 14px;
    height: 14px;
    background: var(--teal);
  }
  .brand__name {
    font-size: 28px;
    font-weight: 500;
    letter-spacing: 1.5px;
    color: var(--ink-grey);
  }

  .back__panel {
    position: absolute;
    inset: 0;
    width: 100%;
    height: 100%;
  }
  .back__panel polygon { fill: var(--teal); }

  .holder {
    position: absolute;
    left: 213px;
    top: 147px;
    color: var(--name-white);
    font-size: 16px;
    font-weight: 600;
    letter-spacing: 1px;
    text-transform: uppercase;
  }
  .holder__title {
    font-size: 10px;
    vertical-align: top;
    margin-left: 3px;
  }

  .contact {
    position: absolute;
    right: 21px;
    top: 213px;
    list-style: none;
    text-align: right;
    color: var(--ink-grey);
    font-size: 12.5px;
    font-weight: 500;
    letter-spacing: 1px;
    line-height: 17.5px;
    text-transform: uppercase;
  }
  .contact__dot {
    display: inline-block;
    width: 9px;
    height: 9px;
    border-radius: 50%;
    background: var(--ink-grey);
    margin-right: 3px;
    vertical-align: -1px;
  }
</style>
</head>
<body>
  <section class="card card--front" aria-label="Card front">
    <div class="brand">
      <span class="brand__square"></span>
      <span class="brand__name">QUORVANTIS</span>
    </div>
  </section>

  <section class="card card--back" aria-label="Card back">
    <svg class="back__panel" viewBox="0 0 548 305" preserveAspectRatio="none" aria-hidden="true">
      <polygon points="0,0 548,0 548,2 265,305 0,305"/>
    </svg>
    <p class="holder">Dana Mercer<span class="holder__title">CEO</span></p>
    <ul class="contact">
      <li>1-800-555-0148, ext. 700</li>
      <li>dana@quorvantis.example</li>
      <li>www.quorvantis.example</li>
      <li><span class="contact__dot"></span>@quorvantis</li>
    </ul>
  </section>
</body>
</html>
```